Snapnook needs You

Help us create an inviting, amazing, sleek, simple, clear landing page for a picture-memory-social connection site!

Business Name: SnapNook
Industry: Social Networking and Creativity through Pictures
A web platform for and about a community that is driven by a passion for sharing, caring, bonding, collaborating, creating and earning with pictures, through pictures and other related creative activities. This is going to be a great site for all creative artists-photographers, artists, graphic artists to express their work and their creativity.

The main focus of the site is - CONNECTIONS.
This will be uncoded.

Desired Website Screen Size
1024x768... Widescreen/Landscape orientation, is what we mean... So it fits on a CPU screen.

Desired look and feel and message
Look: Visitor should feel immersed in the page, in the world the page creates, simple, elegant, sophisticated, contemporary. We really like a clean uncluttered look.

Special mention: By the way we love the marketing genius who thought up this branding for velu yogurt where they used the two dots above the o to create a branding effect that made this brand instantly identifiable. http://www.velu-dairy.ca/en/

The two dots by themselves without having even the name present brings up the whole brand now. The dots are used above all the ingredients of the yogurt creating friendly figures, and above people in commercials-bringing the people onto the side of "team" velu. Snapnook may have a character created or something distinctive in the letters in the name created to brand the site as well.

Feel: Engaging; Magical without being corny, here is a link to give an example look and feel but please do not be hindered in your creativity by this suggestion. We love all creative angles.
http://artscrapheap.com/graphic/5820317-camera-film-roll-blue-background

Message: Life and memories and connections through pictures.

Target audience:
The site is focused on pictures but not confined to photography enthusiasts (although they are an integral part of the site). Customers/Visitors will include families, corporates and the younger generation - all age groups, all class, everyone with pictures to express, memories to share.

Website design we like:
http://morvantstudio.com/work/northern-ballet-guild/
http://morvantstudio.com/work/pixelhop/

What colors do we want to see on our landing page?
We would like the background to be grey or blue since it is grey is picture neutral colour and blue highlights pictures well and we also like blue and silver, which can be integrated into the theme. Also like green. But please do not let these instructions limit your creativity. We are open to new ideas and colours.

Predetermined Concepts if any:
We have a concept in mind and we think it would be cool to have an interface for the user through the back of a camera on the landing page -This could be used to create a scene or world the visitor feels a part of or is immersed into. The back screen of the camera may act as a screen for the slideshow of featured pictures on the site.

Content on the Page:
Photo Gallery with full screen, thumbnail view, zoom option etc.
Prominent but short introductory message
Sign in / Login Options
Links: Home Page; About; Info/Help; Contact Us; Privacy Policy; Terms of Use
At the bottom of the page: Follow Me/Like/Workfolio...social buttons.

Please feel free to add any other element to the landing page that you think might add to the effect of simple yet amazing look -clean, simple, uncluttered, sophisticated, stylish, inviting and engaging.
The concept is a guideline, but we would like you to be as creative as you can, even if it meant stepping out of these guidelines - rethink design, style, content if you like. We believe in bringing a solution in an innovative yet simple and elegant style. Something a visitor would be intrigued enough to explore and the guest would feel comfortable enough taking that step forward to have fun on the site. If you believe in the same, and you have the skill then you will have what we need. Good luck, go for it and we are excited to see what the amazing designers on this amazing site have to offer.
If you have any questions please free to ask.
Updates

HI wanted to send an update that this project design has been guaranteed.

Our site will be one to celebrate and showcase imagination as well as connection.  We would love to see what you create. Keep in mind our site will showcase all creativity, photographs, artists, graphic artists so this would be a benefit you may want to take advantage of in the future, a place where, if you so choose, you could gain exposure for your work. Therefore, even if you do not win the design project there is possible future benefit.

Imagination is everything.
Imagination encircles the world.-Harwood

Reason: We are giving the designers who accepted invites but have not yet submitted a chance to finish their submissions and the ones who are working on revisions a chance to finish those:)

Hello everyone,

Due to time constraints we must come to a decision sooner than the deadline of 28th. 

So, please try to submit any new designs or modifications to the old ones before the 26th. We are very thankful to all of you who have participated - for your designs, enthusiasm and kind words. 

Good luck! :)

• Thank you for the interest shown and your submissions! Designers who have submitted up until now have shown great potential. We are VERY excited with the quality of work and designs.

We want to add that Snapnook is not exclusively for the photographers. The site is for every person who may have a picture to store, organise, use or share - whether publicly or with only a few friends and family.

Snapnook is about allowing people to take control of their creativity. It is about providing tools to our users so that they can build their own connections and social network... of friends, family, fans, clients, ideas, thoughts, emotions etc. through pictures without worrying about their privacy or control over their creations.

With this update we want to encourage others to go beyond the camera theme. Do not let us restrict your creativity. Let YOUR OWN ideas take over if that’s what you think will best convey the message and will appeal to the users.

```html
<!DOCTYPE html>
<html lang="en">
<head>
<meta charset="utf-8">
<title>SnapNook – Life, memories and connections through pictures</title>
<link rel="stylesheet" href="https://fonts.googleapis.com/css2?family=Open+Sans:wght@400;600;700;800&display=swap">
<style>
  :root {
    --bg-deep: #06137a;
    --bg-mid: #1236c4;
    --bg-glow: #2a5ae8;
    --band: rgba(6, 22, 110, 0.55);
    --nav-top: #1a78c8;
    --nav-bottom: #063c8c;
    --nav-active-top: #3aa6e6;
    --nav-active-bottom: #0a5cb0;
    --nav-line: #5fb6f0;
    --teal: #2aa3c9;
    --title-blue: #1e8fe6;
    --silver: #e6e9ee;
    --field: #ffffff;
    --button-blue: #0a6cc0;
    --button-dark: #074f92;
    --footer-grey: #b9b9b9;
    --footer-dark: #585858;
    --footer-text: #2c2c2c;
    --social-blue: #1a9cf0;
    --ink-light: #ffffff;
    --card-amber-ink: #a4a8c8;
    --card-center-ink: #2a2a2a;
    --card-slate-ink: #2aa39a;
    --accent-cyan: #29d0f0;
  }

  * { box-sizing: border-box; margin: 0; padding: 0; }

  html, body {
    width: 1200px;
    height: 900px;
    overflow: hidden;
  }

  body {
    position: relative;
    font-family: "Open Sans", Arial, sans-serif;
    background:
      radial-gradient(ellipse 70% 55% at 50% 45%, var(--bg-glow) 0%, var(--bg-mid) 45%, var(--bg-deep) 100%);
    color: var(--ink-light);
  }

  /* ---------- Header ---------- */
  .brand-name {
    position: absolute;
    left: 33px;
    top: 6px;
    font-size: 78px;
    font-weight: 800;
    letter-spacing: -3px;
    color: var(--silver);
    line-height: 1;
  }

  .brand-tagline {
    position: absolute;
    left: 19px;
    top: 120px;
    font-size: 24px;
    font-weight: 600;
    line-height: 28px;
    color: var(--teal);
  }

  .mascot-art {
    position: absolute;
    left: 436px;
    top: 58px;
    width: 218px;
    height: 128px;
    border-radius: 18px;
    background: linear-gradient(135deg, #4aa6f0 0%, #9cc8ea 45%, #4c4c58 100%);
  }

  .login {
    position: absolute;
    right: 16px;
    top: 16px;
    width: 210px;
  }
  .login-row {
    display: flex;
    justify-content: flex-end;
    align-items: center;
    gap: 6px;
    margin-bottom: 4px;
  }
  .login-label {
    font-size: 14px;
    font-weight: 700;
    color: var(--ink-light);
  }
  .login-field {
    width: 122px;
    height: 16px;
    background: var(--field);
    border: none;
  }
  .login-button {
    display: block;
    margin: 10px 0 0 auto;
    width: 66px;
    height: 19px;
    background: linear-gradient(var(--button-blue), var(--button-dark));
    border: 1px solid #7cc4f2;
    font: 700 13px "Open Sans", Arial, sans-serif;
    color: var(--ink-light);
  }

  .search {
    position: absolute;
    left: 764px;
    top: 178px;
    width: 158px;
    height: 21px;
    border-radius: 11px;
    background: var(--field);
    display: flex;
    align-items: center;
    padding: 0 6px 0 10px;
    justify-content: space-between;
  }
  .search-text {
    font-size: 12px;
    color: #8a8a8a;
  }

  .signup {
    position: absolute;
    left: 1026px;
    top: 172px;
    width: 106px;
    height: 106px;
    border-radius: 50%;
    background: radial-gradient(circle at 50% 35%, #1f5cc8, #0a2a8a 75%);
    box-shadow: 0 0 10px rgba(0, 0, 40, 0.7);
    display: flex;
    align-items: center;
    justify-content: center;
    text-align: center;
    font-size: 27px;
    font-weight: 600;
    line-height: 30px;
    color: #d8dde6;
  }

  /* ---------- Navigation ---------- */
  .main-nav {
    position: absolute;
    left: 29px;
    top: 206px;
    width: 906px;
    height: 35px;
    display: flex;
    border: 1px solid var(--nav-line);
  }
  .nav-item {
    flex: 1;
    display: flex;
    align-items: center;
    justify-content: center;
    background: linear-gradient(var(--nav-top), var(--nav-bottom));
    border-right: 1px solid var(--nav-line);
    font-size: 18px;
    font-weight: 700;
    letter-spacing: -1.2px;
    color: var(--ink-light);
  }
  .nav-item:last-child { border-right: none; }
  .nav-item.is-active {
    background: linear-gradient(var(--nav-active-top), var(--nav-active-bottom));
  }

  /* ---------- Gallery ---------- */
  .gallery-title {
    position: absolute;
    left: 0;
    top: 254px;
    width: 1200px;
    text-align: center;
    font-size: 50px;
    font-weight: 700;
    letter-spacing: -1px;
    color: var(--title-blue);
    text-shadow: 0 3px 6px rgba(0, 0, 30, 0.8);
  }

  .gallery-band {
    position: absolute;
    left: 0;
    top: 322px;
    width: 1200px;
    height: 355px;
    background: var(--band);
  }

  .gallery-card {
    position: absolute;
    display: flex;
    align-items: center;
  }
  .card-left {
    left: 110px;
    top: 384px;
    width: 288px;
    height: 263px;
    background: linear-gradient(135deg, #9a7434, #7c6238);
    padding-left: 70px;
  }
  .card-right {
    left: 797px;
    top: 384px;
    width: 274px;
    height: 263px;
    background: linear-gradient(135deg, #2a3c5e, #1e2e52);
    padding-left: 80px;
  }
  .card-center {
    left: 398px;
    top: 332px;
    width: 399px;
    height: 333px;
    justify-content: center;
    gap: 14px;
    background: radial-gradient(ellipse 55% 55% at 50% 48%, #ffffff 0%, #d6eef8 35%, #8a9aa4 75%, #6e6e6e 100%);
    box-shadow: 0 0 12px rgba(0, 0, 30, 0.5);
  }
  .card-name {
    font-size: 38px;
    font-weight: 600;
    letter-spacing: -1px;
  }
  .card-left .card-name { color: var(--card-amber-ink); }
  .card-right .card-name { color: var(--card-slate-ink); }
  .card-center .card-name { color: var(--card-center-ink); font-size: 40px; }
  .card-mark {
    width: 30px;
    height: 30px;
    background: var(--accent-cyan);
  }

  .gallery-arrow {
    position: absolute;
    top: 493px;
    width: 52px;
    height: 52px;
  }
  .arrow-prev { left: 323px; }
  .arrow-next { left: 817px; }

  /* ---------- Feedback ---------- */
  .feedback {
    position: absolute;
    left: 338px;
    top: 691px;
    width: 522px;
    height: 44px;
    background: #dcdcdc;
    border: 1px solid #c2c2c2;
    padding: 5px 7px;
    font-size: 12px;
    color: #7a7a7a;
  }
  .feedback-submit {
    position: absolute;
    left: 775px;
    top: 742px;
    width: 85px;
    height: 28px;
    background: linear-gradient(#0b5fa6, #063e78);
    border: 1px solid #5fb6f0;
    font: 700 13px "Open Sans", Arial, sans-serif;
    color: var(--ink-light);
  }

  /* ---------- Footer ---------- */
  .site-footer {
    position: absolute;
    left: 103px;
    top: 804px;
    width: 996px;
    height: 96px;
  }
  .footer-panel {
    height: 70px;
    background: linear-gradient(#c8c8c8, var(--footer-grey));
    display: flex;
    align-items: center;
    justify-content: flex-end;
    padding-right: 14px;
    gap: 8px;
  }
  .follow-label {
    font-size: 19px;
    color: var(--footer-text);
    margin-right: 4px;
  }
  .social-button {
    height: 32px;
    padding: 0 9px;
    display: flex;
    align-items: center;
    background: var(--social-blue);
    border: 2px solid #ffffff;
    font-size: 12px;
    font-weight: 700;
    color: var(--ink-light);
  }
  .footer-bar {
    height: 26px;
    background: var(--footer-dark);
    padding-left: 36px;
    display: flex;
    align-items: center;
    font-size: 13px;
    color: #f0f0f0;
  }
  .footer-mascot-art {
    position: absolute;
    left: 132px;
    top: 764px;
    width: 166px;
    height: 100px;
    border-radius: 14px;
    background: linear-gradient(135deg, #d0d0d0 0%, #9a9a9a 50%, #3e3e3e 100%);
  }
</style>
</head>
<body>

<header class="site-header">
  <div class="brand-name">SnapNook</div>
  <p class="brand-tagline">Life, memories and connections<br>through pictures.</p>
  <div class="mascot-art" role="img" aria-label="Mascot character holding a camera beside a strip of instant photos"></div>

  <form class="login">
    <div class="login-row"><span class="login-label">Username:</span><input class="login-field" type="text" aria-label="Username"></div>
    <div class="login-row"><span class="login-label">Password:</span><input class="login-field" type="password" aria-label="Password"></div>
    <button class="login-button" type="button">Log In</button>
  </form>

  <div class="search">
    <span class="search-text">...Search</span>
    <svg width="14" height="14" viewBox="0 0 14 14" aria-hidden="true">
      <circle cx="8" cy="6" r="4.2" fill="none" stroke="#555" stroke-width="1.8"/>
      <line x1="5" y1="9" x2="1.5" y2="12.5" stroke="#555" stroke-width="2" stroke-linecap="round"/>
    </svg>
  </div>

  <div class="signup">Sign<br>Up</div>

  <nav class="main-nav">
    <span class="nav-item is-active">Home</span>
    <span class="nav-item">About</span>
    <span class="nav-item">Info</span>
    <span class="nav-item">Contact Us</span>
    <span class="nav-item">Privacy Policy</span>
    <span class="nav-item">Terms of Use</span>
  </nav>
</header>

<main>
  <h1 class="gallery-title">Popular Gallery</h1>
  <div class="gallery-band"></div>

  <div class="gallery-card card-left"><span class="card-name">Tunehive</span></div>
  <div class="gallery-card card-right"><span class="card-name">Pixelmoor</span></div>
  <div class="gallery-card card-center"><span class="card-name">Brightwell</span><span class="card-mark"></span></div>

  <svg class="gallery-arrow arrow-prev" viewBox="0 0 52 52" aria-label="Previous">
    <circle cx="26" cy="26" r="24" fill="#1a5ae0" stroke="#0a1a50" stroke-width="3"/>
    <polyline points="30,15 19,26 30,37" fill="none" stroke="#0a1a50" stroke-width="5" stroke-linecap="round" stroke-linejoin="round"/>
  </svg>
  <svg class="gallery-arrow arrow-next" viewBox="0 0 52 52" aria-label="Next">
    <circle cx="26" cy="26" r="24" fill="#1a5ae0" stroke="#0a1a50" stroke-width="3"/>
    <polyline points="22,15 33,26 22,37" fill="none" stroke="#0a1a50" stroke-width="5" stroke-linecap="round" stroke-linejoin="round"/>
  </svg>

  <div class="feedback">Post feedback...</div>
  <button class="feedback-submit" type="button">Submit</button>
</main>

<footer class="site-footer">
  <div class="footer-panel">
    <span class="follow-label">Follow us on...</span>
    <span class="social-button">Kinboard</span>
    <span class="social-button">Workfolio</span>
    <span class="social-button">Chirpline</span>
  </div>
  <div class="footer-bar">© Copyright SnapNook 2012</div>
</footer>
<div class="footer-mascot-art" role="img" aria-label="Grey mascot character holding a camera beside a strip of photos"></div>

</body>
</html>
```